Tarvel Ridge LLC

Need Professional Business cards for New Investment Fund

Target Market(s)

High Quality investors

Industry/Entity Type

Financial

Contact Information for Business Card

Phone Number +1 555 284 6193
Name Pavel Orlinsky
Title Fund Manager
email po@FundTarvel.example
Website www.FundTarvel.example

Colors

Designer to choose colors to be used in the design.

Requirements
Must have
• Must have our Logo and all of the above. Must be made so lettering and loge can be raised

```html
<!DOCTYPE html>
<html lang="en">
<head>
<meta charset="utf-8">
<title>Tarvel Ridge LLC – Business Cards</title>
<link rel="stylesheet" href="https://fonts.googleapis.com/css2?family=Figtree:wght@400;500&display=swap">
<style>
  :root {
    --stage: #021827;
    --card: #082c42;
    --green: #5cb84a;
    --ink: #e6edf1;
    --mark: #4a5a48;
  }
  * { margin: 0; padding: 0; box-sizing: border-box; }
  html, body {
    width: 1200px;
    height: 655px;
    overflow: hidden;
    background: var(--stage);
    font-family: "Figtree", Arial, sans-serif;
  }
  .sheet {
    position: relative;
    width: 1200px;
    height: 655px;
    display: flex;
    gap: 40px;
    justify-content: center;
    align-items: center;
  }
  .card {
    position: relative;
    width: 540px;
    height: 350px;
    background: var(--card);
    overflow: hidden;
  }
  .card__name {
    position: absolute;
    left: 23px;
    top: 50px;
    font-size: 29px;
    font-weight: 400;
    color: var(--ink);
    letter-spacing: 0.2px;
  }
  .card__title {
    position: absolute;
    left: 0;
    top: 90px;
    width: 189px;
    height: 24px;
    padding-left: 23px;
    background: var(--green);
    color: var(--ink);
    font-size: 16px;
    line-height: 24px;
  }
  .card__contact {
    position: absolute;
    right: 28px;
    bottom: 54px;
    text-align: right;
    color: var(--ink);
    font-size: 20px;
    line-height: 27px;
    list-style: none;
  }
  .brand {
    position: absolute;
    left: 0;
    right: 0;
    top: 150px;
    display: flex;
    justify-content: center;
    align-items: center;
    gap: 10px;
  }
  .brand__square {
    width: 14px;
    height: 14px;
    background: var(--green);
  }
  .brand__name {
    font-size: 26px;
    font-weight: 500;
    color: var(--green);
    letter-spacing: 0.5px;
  }
  .card__bar {
    position: absolute;
    left: 0;
    right: 0;
    bottom: 12px;
    height: 20px;
    background: var(--green);
  }
</style>
</head>
<body>
  <main class="sheet">
    <section class="card card--front">
      <h1 class="card__name">Pavel Orlinsky</h1>
      <p class="card__title">Title Fund Manager</p>
      <ul class="card__contact">
        <li>+1 555 284 6193</li>
        <li>po@FundTarvel.example</li>
        <li>www.FundTarvel.example</li>
      </ul>
    </section>
    <section class="card card--back">
      <div class="brand">
        <span class="brand__square"></span>
        <span class="brand__name">Tarvel Ridge</span>
      </div>
      <div class="card__bar"></div>
    </section>
  </main>
</body>
</html>
```